Broschüre für Trainer für Resilienz
Zielgruppe
Wir sind ein Zusammenschluss von zwei selbstständigen Trainern, welche sich spezialisiert haben auf den Bereich Resilienz in Unternehmen.
Insgesamt haben wir hierfür 4 Säulen erarbeitet:
1. Resilienz - Training
2. Psychologische Beratung
3. Burnout - Prophylaxe
4. Weiterbildungen
Weitere Informationen finden Sie in der angehängten Datei mit dem Titel 'flyer_Inhalt'.
Als Zielgruppe haben wir mittelständische und große Unternehmen im Blick, hierbei jeweils die Mitarbeiter und Führungskräfte
Aufgabenstellung
Wir stellen uns eine Broschüre im DIN-A4 - Format vor, 6 Seiten mit Wickelfalz.
Eine Broschüre, welche bei Kunden großen Anklang gefunden hat, war meine Dozent4.1 - Broschüre, welche ich als Beispiel ebenfalls hochgeladen habe.
Nach ein paar Missverständnissen möchte ich das Format an dieser Stelle genauer beschreiben:
Es geht um einen Flyer/ eine Broschüre, welche im DIN-A4-Format gestaltet wird. Hierbei nicht ein DIN-A4-Format im Querformat, sondern DREI DIN-A4-Seiten, welche mit einer Wickelfalz verbunden sind und somit 6 DIN-A4-Flächen zum Bedrucken bilden.

```html
<!DOCTYPE html>
<html lang="de">
<head>
<meta charset="utf-8">
<title>Standfest Coaching – Broschüre</title>
<link href="https://fonts.googleapis.com/css2?family=Open+Sans:wght@300;400;600&display=swap" rel="stylesheet">
<style>
:root{
  --blue:#1a4a8e;
  --dark:#3a3a3d;
  --tile:#e3e3e7;
  --tile-text:#4a4a4e;
  --icon:#5c5c62;
  --caption:rgba(222,220,228,.78);
  --white:#ffffff;
  --ink:#222226;
  --muted:#6a6a70;
  --bullet:#d8d8dc;
}
*{margin:0;padding:0;box-sizing:border-box}
html,body{width:1200px;height:566px;overflow:hidden;background:var(--dark)}
body{font-family:'Open Sans',sans-serif;position:relative}
.panel{position:absolute;top:0;height:566px;overflow:hidden}
.panel--pillars{left:0;width:400px;background:var(--dark)}
.panel--trainers{left:400px;width:399px;background:var(--white)}
.panel--cover{left:801px;width:399px;background:var(--dark)}

.photo{position:absolute;left:0;width:100%}
.photo--team{top:0;height:242px;background:linear-gradient(135deg,#d9dde3 0%,#b7a79a 45%,#8a94a6 100%)}
.photo--trainer-a{top:0;height:243px;background:radial-gradient(circle at 70% 40%,#3b2f36 0 22%,transparent 40%),linear-gradient(120deg,#c9a777,#9c7c55)}
.photo--trainer-b{top:243px;height:234px;background:radial-gradient(circle at 70% 45%,#2a2528 0 25%,transparent 45%),linear-gradient(120deg,#57495c,#3d3442)}
.photo--cover{top:0;height:403px;background:radial-gradient(circle at 65% 45%,#2b2b2d 0 30%,transparent 55%),linear-gradient(160deg,#4a4a4c,#2e2e30)}

.band{position:absolute;left:0;top:242px;width:400px;height:80px;background:var(--blue);padding:24px 0 0 55px;color:var(--white);font-weight:300;font-size:21.5px;line-height:25px}
.band strong{font-weight:600}

.pillar-grid{position:absolute;left:55px;top:335px;width:272px;height:197px}
.pillar{position:absolute;width:133px;height:95px;background:var(--tile);display:flex;flex-direction:column;align-items:center;justify-content:center;text-align:center;color:var(--tile-text);font-size:12.5px;line-height:14px;font-weight:400}
.pillar svg{margin-bottom:10px}
.pillar--tl{left:0;top:0}
.pillar--tr{left:139px;top:0}
.pillar--bl{left:0;top:102px}
.pillar--br{left:139px;top:102px}
.pillar-grid .notches{position:absolute;left:0;top:0}

.section-title{position:absolute;left:27px;top:20px;color:var(--white);font-weight:300;font-size:22.5px}
.caption{position:absolute;left:0;width:231px;background:var(--caption);padding:0 18px 0 28px;color:var(--ink)}
.caption--a{top:161px;height:82px;padding-top:16px}
.caption--b{top:394px;height:83px;padding-top:14px;width:233px;padding-left:30px}
.caption h3{font-size:9.5px;font-weight:400;margin-bottom:6px}
.caption p{font-size:5.5px;line-height:9.3px}

.contact{position:absolute;left:28px;top:496px;display:grid;grid-template-columns:48px 145px 130px;font-size:9px;line-height:12.8px;color:var(--ink)}
.contact .label{color:var(--muted)}

.brand-box{position:absolute;left:0;top:337px;width:343px;height:67px;background:var(--blue);display:flex;align-items:center;padding-left:29px}
.brand-name{color:var(--white);font-weight:400;font-size:29px;white-space:nowrap}

.benefits{position:absolute;left:95px;top:431px;list-style:none;color:var(--bullet);font-size:11px;line-height:16px}
.benefits li{position:relative;padding-left:27px;margin-bottom:17px}
.benefits li svg{position:absolute;left:0;top:3px}
.benefits li.strong{font-weight:600}
</style>
</head>
<body>

<section class="panel panel--pillars">
  <div class="photo photo--team" role="img" aria-label="Foto: Team legt die Hände übereinander"></div>
  <h2 class="band">Die vier Säulen für Ihr<br><strong>resilientes</strong> Unternehmen</h2>
  <div class="pillar-grid">
    <div class="pillar pillar--tl"><svg width="12" height="14" viewBox="0 0 12 14"><path d="M6 0 12 2v5c0 4-3 6-6 7C3 13 0 11 0 7V2z" fill="var(--icon)"/></svg>Resilienz-Training</div>
    <div class="pillar pillar--tr"><svg width="12" height="14" viewBox="0 0 12 14"><path d="M6 0 12 2v5c0 4-3 6-6 7C3 13 0 11 0 7V2z" fill="var(--icon)"/></svg>Burnout-<br>Prophylaxe</div>
    <div class="pillar pillar--bl"><svg width="12" height="14" viewBox="0 0 12 14"><path d="M6 0 12 2v5c0 4-3 6-6 7C3 13 0 11 0 7V2z" fill="var(--icon)"/></svg>Psychologische<br>Beratung</div>
    <div class="pillar pillar--br"><svg width="12" height="14" viewBox="0 0 12 14"><path d="M6 0 12 2v5c0 4-3 6-6 7C3 13 0 11 0 7V2z" fill="var(--icon)"/></svg>Weiterbildungen</div>
    <svg class="notches" width="272" height="197" viewBox="0 0 272 197">
      <path d="M133 28 140 36 133 44z" fill="var(--tile)"/>
      <path d="M118 95 126 87 134 95z" fill="var(--tile)"/>
      <path d="M179 102 187 110 195 102z" fill="var(--tile)"/>
      <path d="M139 130 132 138 139 146z" fill="var(--tile)"/>
    </svg>
  </div>
</section>

<section class="panel panel--trainers">
  <div class="photo photo--trainer-a" role="img" aria-label="Porträtfoto der Trainerin"></div>
  <h2 class="section-title">Ihre Trainer</h2>
  <div class="caption caption--a">
    <h3>Dipl. Psych. Sabine Korthaus</h3>
    <p>Inhaberin und Leiterin der Praxisgemeinschaft am Lindenhof, Psychologische Psychotherapeutin, Kinder- und Jugendlichen-Psychotherapie, Zertifizierte Trainerin für Autogenes Training, Mehrjährige Erfahrung als Trainerin</p>
  </div>
  <div class="photo photo--trainer-b" role="img" aria-label="Porträtfoto des Trainers"></div>
  <div class="caption caption--b">
    <h3>Jonas Martin Wehling, M.A.</h3>
    <p>Mehrjährige Erfahrung als Trainer, Zertifizierter Mediator mit mehrjähriger Berufserfahrung, Psychotherapeut in der Ausbildung zum Kinder- und Jugendlichenpsychotherapeuten, Internationale Berufs- und Studienerfahrung</p>
  </div>
  <div class="contact">
    <span class="label">Telefon</span><span>02104 61 38 402</span><span class="label">Post</span>
    <span class="label">Fax</span><span>02104 61 38 409</span><span>standfest-coaching</span>
    <span class="label">E-Mail</span><span>info@standfest-coaching.de</span><span>Lindenweg 14</span>
  </div>
</section>

<section class="panel panel--cover">
  <div class="photo photo--cover" role="img" aria-label="Foto: Geschäftsmann mit erhobener Faust vor dunklem Hintergrund"></div>
  <div class="brand-box"><span class="brand-name">Standfest Coaching</span></div>
  <ul class="benefits">
    <li><svg width="12" height="14" viewBox="0 0 12 14"><path d="M6 0 12 2v5c0 4-3 6-6 7C3 13 0 11 0 7V2z" fill="var(--icon)"/></svg>Leistungsfähige Mitarbeiter sichern<br>den Erfolg Ihres Unternehmens.</li>
    <li class="strong"><svg width="12" height="14" viewBox="0 0 12 14"><path d="M6 0 12 2v5c0 4-3 6-6 7C3 13 0 11 0 7V2z" fill="var(--icon)"/></svg>Nutzen Sie die Vorteile der gesetzlich<br>geförderten Gesundheitsvorsorge für<br>Ihr Team.</li>
  </ul>
</section>

</body>
</html>
```